Business Card Design

I am a Special Event Consultant,I arrange and organise Special Events - Product Launches,Sponsorship and Product Displays.

I would like the RTV to be a feature of the design with 'Special Event Services" underneath - keep it very simple but creative using this information. So it is just the letters "RTV" with Event Services underneath.

(Simple Colours - Silver, Black, Grey - no bright colours - We work for Valtoria Drenn,KDX, Lyndrel So it is class and classic.)

Only my Name and mobile on the front.

Contact Information for Business Card

FRONT
Tess Varnholt
Tel: 0436 218907

BACK
Email: tess@rtveventservices.example.au

2807 Wexbury Heights,83 Pollard Street
NORTHVALE.Vic.3158.

```html
<!DOCTYPE html>
<html lang="en">
<head>
<meta charset="utf-8">
<title>RTV Event Services – Business Card</title>
<link rel="stylesheet" href="https://fonts.googleapis.com/css2?family=Questrial&display=swap">
<style>
  :root {
    --backdrop: #e4e4e4;
    --charcoal: #262626;
    --silver: #b8b8bb;
    --paper: #ffffff;
    --band-grey: #efefef;
    --ink: #1c1c1c;
    --ink-soft: #555555;
    --rule: #6a6a6a;
    --on-dark: #e6e6e8;
  }
  * { box-sizing: border-box; margin: 0; padding: 0; }
  html, body { width: 1200px; height: 800px; overflow: hidden; }
  body {
    background: var(--backdrop);
    font-family: "Questrial", "Century Gothic", sans-serif;
    position: relative;
  }
  .card {
    position: absolute;
    top: 235px;
    width: 540px;
    height: 330px;
    border-radius: 8px;
    overflow: hidden;
    box-shadow: 0 3px 10px rgba(0,0,0,0.18);
  }
  .card::before {
    content: "";
    position: absolute;
    left: 0; top: 0; bottom: 0;
    width: 24px;
  }

  /* Back of card */
  .card--back { left: 40px; background: var(--charcoal); }
  .card--back::before { background: var(--silver); }
  .contact-list {
    position: absolute;
    left: 62px;
    top: 96px;
    list-style: none;
    color: var(--on-dark);
    font-size: 15px;
    letter-spacing: 0.5px;
    line-height: 1.3;
    text-transform: uppercase;
  }
  .contact-item { display: flex; gap: 12px; align-items: flex-start; margin-bottom: 12px; }
  .contact-item .icon { flex: none; width: 22px; height: 22px; }
  .contact-item--email { font-size: 13px; align-items: center; }

  /* Front of card */
  .card--front { left: 620px; background: var(--paper); }
  .card--front::before { background: var(--charcoal); z-index: 2; }
  .lower-band {
    position: absolute;
    left: 0; right: 0; bottom: 0;
    height: 100px;
    background: var(--band-grey);
  }
  .holder {
    position: absolute;
    left: 52px;
    top: 88px;
    right: 40px;
  }
  .holder-name {
    font-weight: 400;
    font-size: 30px;
    letter-spacing: 1px;
    color: var(--ink);
    text-transform: uppercase;
    line-height: 1;
  }
  .holder-role {
    display: flex;
    align-items: center;
    gap: 6px;
    margin-top: 4px;
    font-size: 10px;
    letter-spacing: 1.5px;
    color: var(--ink-soft);
    text-transform: uppercase;
  }
  .holder-role::after {
    content: "";
    flex: 1;
    height: 1px;
    background: var(--rule);
  }
  .phone {
    position: absolute;
    left: 52px;
    top: 170px;
    display: flex;
    align-items: center;
    gap: 14px;
    font-size: 21px;
    letter-spacing: 1px;
    color: var(--ink);
  }
  .phone .icon { width: 20px; height: 20px; }
  .brand {
    position: absolute;
    right: 26px;
    bottom: 14px;
    text-align: right;
    color: var(--ink);
    text-transform: uppercase;
  }
  .brand-name {
    font-size: 30px;
    letter-spacing: 8px;
    margin-right: -8px;
    line-height: 1;
  }
  .tagline {
    margin-top: 6px;
    font-size: 11px;
    letter-spacing: 1.5px;
    color: var(--ink-soft);
  }
</style>
</head>
<body>

  <section class="card card--back" aria-label="Card back">
    <ul class="contact-list">
      <li class="contact-item">
        <svg class="icon" viewBox="0 0 22 22" aria-hidden="true">
          <circle cx="11" cy="11" r="10" fill="none" stroke="#e6e6e8" stroke-width="1.6"/>
          <path d="M11 5.5a3.6 3.6 0 0 0-3.6 3.6c0 2.7 3.6 7 3.6 7s3.6-4.3 3.6-7A3.6 3.6 0 0 0 11 5.5z" fill="#e6e6e8"/>
          <circle cx="11" cy="9.1" r="1.3" fill="#262626"/>
        </svg>
        <span>2807 Wexbury Heights<br>83 Pollard Street<br>Northvale.Vic.3158</span>
      </li>
      <li class="contact-item contact-item--email">
        <svg class="icon" viewBox="0 0 22 22" aria-hidden="true">
          <circle cx="11" cy="11" r="10" fill="none" stroke="#e6e6e8" stroke-width="1.6"/>
          <rect x="5.5" y="7.5" width="11" height="7.5" fill="#e6e6e8"/>
          <path d="M5.5 7.5l5.5 4.2 5.5-4.2" fill="none" stroke="#262626" stroke-width="1.1"/>
        </svg>
        <span>tess@rtveventservices.example.au</span>
      </li>
    </ul>
  </section>

  <section class="card card--front" aria-label="Card front">
    <div class="lower-band"></div>
    <div class="holder">
      <h1 class="holder-name">Tess Varnholt</h1>
      <p class="holder-role">Event Consultant</p>
    </div>
    <p class="phone">
      <svg class="icon" viewBox="0 0 20 20" aria-hidden="true">
        <circle cx="10" cy="10" r="9" fill="#f4f4f4" stroke="#777" stroke-width="1.2"/>
        <path d="M7.2 5.2l1.6 2.4-1 1.1c.6 1.4 1.6 2.4 3 3l1.1-1 2.4 1.6-.9 1.7c-3.6-.4-6.5-3.3-6.9-6.9z" fill="#333"/>
      </svg>
      <span>0436 218907</span>
    </p>
    <div class="brand">
      <p class="brand-name">RTV</p>
      <p class="tagline">Special Event Services</p>
    </div>
  </section>

</body>
</html>
```